Kelvo App - Live Events Stream

Need mobile first appliation designs for a new location based events and offers application <br/><br/>Will require at least 5 screens creating, namely:<br/><br/>- Landing screen<br/>- Event/Offer listings screen<br/>- Overview of Event/Offer screen<br/>- Chat/Stream for Event/Offer<br/>- Directions for Event/Offer<br/>- Create Event/Offer screen(s)<br/><br/>Will require the design to have a vantor material feel. <br/><br/>See Attached files for further details

Requirements
Must have
• See Doc
Nice to have
• See Doc
Should not have
• See Doc

```html
<!DOCTYPE html>
<html lang="en">
<head>
<meta charset="utf-8">
<title>Kelvo – Live Events Stream</title>
<link href="https://fonts.googleapis.com/css2?family=Poppins:ital,wght@0,400;0,500;0,600;0,700;1,400&display=swap" rel="stylesheet">
<style>
:root{
  --backdrop:#FDDF6A;
  --white:#FFFFFF;
  --ink:#1E1E24;
  --muted:#8A8A94;
  --hairline:#EFEFF3;
  --field:#F7F7F9;
  --accent:#5BD6E1;
  --accent-soft:#C9F1F5;
  --purple:#D07BF5;
  --sun:#FDDF6A;
  --sun-soft:#FFF3C4;
  --sun-text:#F4C93A;
  --bubble-grey:#F1F0F5;
}
*{box-sizing:border-box;margin:0;padding:0}
html,body{width:730px;height:1200px;overflow:hidden}
body{background:var(--backdrop);font-family:'Poppins',sans-serif;color:var(--ink);position:relative}
svg.icon{width:7px;height:7px;fill:none;stroke:currentColor;stroke-width:1.6;stroke-linecap:round;stroke-linejoin:round;flex:none}

.screen{position:absolute;width:144px;height:310px;background:var(--white);border-radius:18px;overflow:hidden;box-shadow:0 6px 18px rgba(0,0,0,.08)}
.status{position:absolute;top:8px;left:13px;right:10px;display:flex;justify-content:space-between;font-size:5px;font-weight:500;z-index:3}
.status .signal{display:flex;gap:2px;align-items:center}
.status .signal i{display:block;width:7px;height:3px;border-radius:1px;background:currentColor}
.screen-title{position:absolute;top:19px;left:7px;font-size:8.5px;font-weight:600}

.tab-bar{position:absolute;left:0;right:0;bottom:10px;height:20px;display:flex;justify-content:space-around;align-items:center;padding:0 6px;color:#9A9AA4;background:var(--white)}
.tab-bar svg.icon{width:8px;height:8px;stroke-width:1.3}
.tab-bar .active{color:var(--accent)}
.tab-bar .me{width:16px;height:16px;border-radius:4px;background:linear-gradient(135deg,#2E8FA0,#D97A4A)}
.home-indicator{position:absolute;bottom:4px;left:50%;width:52px;height:2px;margin-left:-26px;border-radius:2px;background:var(--ink)}

/* event card */
.event-card{position:absolute;left:10px;width:124px}
.event-photo{position:relative;height:58px;border-radius:6px;background:linear-gradient(160deg,#D9D9DB,#7E7F84 55%,#3F4046)}
.event-photo.concert{background:radial-gradient(ellipse at 50% 90%,#E8B12A 0,#6B4A12 35%,#151518 70%)}
.badge{position:absolute;top:5px;right:4px;background:var(--sun);color:var(--white);font-size:4.5px;line-height:6px;padding:2px 9px;border-radius:4px}
.countdown{position:absolute;left:0;right:0;top:24px;text-align:center;color:var(--white);font-size:8px;line-height:10px;font-weight:700;letter-spacing:.4px}
.event-info{position:relative;margin:-14px 4px 0;background:var(--white);border-radius:5px;padding:5px 6px 4px;box-shadow:0 2px 8px rgba(0,0,0,.06)}
.event-info h3{font-size:6.5px;line-height:9px;font-weight:600;margin-bottom:3px}
.meta-row{display:flex;align-items:center;gap:3px;font-size:4.3px;height:10.5px}
.meta-row .avatar{width:6px;height:6px;border-radius:2px;background:#3A3330;flex:none}
.meta-row em{margin-left:auto;color:var(--accent);font-size:4.3px}
.meta-row.place{color:var(--sun-text)}
.meta-row.date{color:var(--purple)}
.attendees{margin-left:auto;display:flex;align-items:center}
.attendees i{width:6px;height:6px;border-radius:1px;background:#4A4A4E;margin-right:-1px}
.attendees b{font-weight:500;background:var(--purple);color:var(--white);font-size:3.6px;padding:1px 2px;border-radius:1px;margin-left:1px}

/* home */
.home-tabs{position:absolute;top:45px;left:7px;display:flex;gap:11px;font-size:6.3px;color:#55555E;white-space:nowrap}
.home-tabs span:first-child{position:relative}
.home-tabs span:first-child::after{content:"";position:absolute;left:11px;top:12px;width:3px;height:3px;border-radius:1px;background:var(--accent)}

/* overview */
.hero{position:absolute;top:0;left:0;right:0;height:103px;background:linear-gradient(170deg,#EDEDEF,#9A9BA0 45%,#4B4C52)}
.hero-title{position:absolute;top:19px;left:0;right:0;text-align:center;color:var(--white);font-size:6.5px}
.hero-back{position:absolute;top:20px;left:9px;color:var(--white)}
.hero .countdown{top:47px;font-size:8.5px}
.dots{position:absolute;top:95px;left:0;right:0;display:flex;justify-content:center;gap:4px}
.dots i{width:3px;height:3px;border:.7px solid var(--sun);border-radius:50%}
.dots i:first-child{background:var(--sun)}
.organizer-band{position:absolute;top:103px;left:0;right:0;height:44px;background:var(--sun-soft);display:flex;align-items:center;gap:6px;padding:0 7px}
.organizer-band .avatar{width:20px;height:20px;border-radius:4px;background:#3A3330}
.organizer-band strong{font-size:6.5px;font-weight:600}
.organizer-band svg{margin-left:auto;color:var(--sun-text);width:8px;height:8px}
.overview-body{position:absolute;top:157px;left:7px;right:7px}
.overview-head{display:flex;justify-content:space-between;align-items:center}
.overview-head h2{font-size:6.8px;font-weight:600}
.overview-head .badge{position:static;padding:2px 10px}
.overview-body p{font-size:5.3px;line-height:8.3px;color:#55555E;margin:6px 0 8px}
.overview-body .meta-row{height:18px;font-size:4.6px}
.overview-body .meta-row svg{width:8px;height:8px}
.view-map{margin-left:auto;text-decoration:underline;color:var(--sun-text)}
.tag{background:var(--sun);color:var(--white);font-size:4.6px;padding:2.5px 5px;border-radius:5px}
.btn-primary{position:absolute;left:50%;width:92px;margin-left:-46px;height:19px;border-radius:4px;background:var(--accent);color:var(--white);font-size:6.5px;font-weight:600;display:flex;align-items:center;justify-content:center;box-shadow:0 3px 8px rgba(91,214,225,.35)}

/* inbox */
.thread{position:absolute;left:7px;right:7px;height:27px;display:flex;gap:4px;border-bottom:.6px solid var(--hairline)}
.thread .avatar{width:20px;height:20px;border-radius:3px;flex:none}
.thread-body{flex:1;min-width:0}
.thread-top{display:flex;align-items:baseline;font-size:6.3px}
.thread-top em{font-size:4.4px;color:var(--accent);margin-left:2px}
.thread-top time{margin-left:auto;font-size:4.5px;font-weight:500}
.thread-msg{display:flex;font-size:5.2px;color:#55555E;margin-top:3px}
.thread-msg.unread{color:var(--ink);font-weight:500}
.unread-count{margin-left:auto;font-size:4px;color:var(--purple);background:#F3E3FB;padding:0 2px;border-radius:1px}

/* chat */
.chat-head{position:absolute;top:17px;left:0;right:0;text-align:center;font-size:6.5px;line-height:9px}
.chat-head strong{display:block;font-size:6.5px;line-height:9px;font-weight:500}
.chat-head em{display:block;font-size:5px;line-height:8px;color:var(--accent)}
.chat-back{position:absolute;top:19px;left:9px;line-height:0}
.chat-more{position:absolute;top:17px;right:10px;color:var(--accent);font-size:8px;letter-spacing:-1px;line-height:8px}
.chat-avatar{position:absolute;top:40px;left:62px;width:20px;height:20px;border-radius:4px;background:#3A3330}
.bubble{position:absolute;border-radius:6px;font-size:4.8px;line-height:7.5px;padding:5px 4px}
.bubble.mine{left:18px;width:93px;background:var(--purple);color:var(--white)}
.bubble.theirs{left:32px;width:93px;background:var(--bubble-grey);color:#55555E;padding-left:4px}
.bubble time{display:block;text-align:right;font-size:3.2px;line-height:4px;margin-top:3px}
.bubble.theirs time{text-align:left}
.chat-face{position:absolute;width:8px;height:8px;border-radius:2px;background:#4A4442}
.composer{position:absolute;top:280px;left:6px;width:104px;height:19px;border:.7px solid #E4D3F3;border-radius:4px;display:flex;align-items:center;gap:4px;padding:0 6px;font-size:5.5px;color:#9A9AA4}
.composer svg{color:var(--purple)}
.send-btn{position:absolute;top:280px;left:114px;width:22px;height:19px;border-radius:4px;background:var(--purple);color:var(--white);display:flex;align-items:center;justify-content:center}

/* search */
.segmented{position:absolute;top:51px;left:8px;right:8px;height:20px;display:flex;gap:2px}
.segmented span{flex:1;display:flex;align-items:center;justify-content:center;font-size:6px;font-weight:500;color:var(--sun-text);border-radius:4px}
.segmented .on{background:var(--sun-soft)}
.search-field{position:absolute;top:82px;left:10px;right:10px;height:19px;background:var(--field);border-radius:4px;display:flex;align-items:center;gap:4px;padding:0 6px;font-size:4.8px;color:var(--muted)}
.search-field svg{color:var(--accent)}
.search-field svg:last-child{margin-left:auto}
.results{position:absolute;top:108px;left:0;right:0;height:172px;overflow:hidden}
.map-area{position:absolute;top:110px;left:10px;right:10px;height:170px;background:linear-gradient(180deg,#F7F7F8,#EFEFF1);border-radius:4px}
.map-card{position:absolute;top:143px;left:20px;width:92px;transform-origin:0 0}
.map-card .event-photo{height:44px}
.map-card .countdown{top:18px;font-size:6px}
.map-card .badge{font-size:3.2px;line-height:4px;padding:1px 6px;top:3px}
.map-card .event-info{margin:-10px 3px 0;padding:4px 5px}
.map-card .event-info h3{font-size:4.8px;line-height:6px;margin-bottom:2px}
.map-card .meta-row{height:8px;font-size:3.2px}
.map-card .meta-row em{font-size:3.2px}
.map-card .meta-row .avatar,.map-card .attendees i{width:4px;height:4px}
.map-card svg.icon{width:4.5px;height:4.5px}
.you-pin{position:absolute;top:206px;left:62px;width:14px;height:14px;border-radius:50%;background:var(--accent-soft);display:flex;align-items:center;justify-content:center;color:var(--accent);box-shadow:0 0 14px 8px rgba(91,214,225,.18)}
.map-pin{position:absolute;top:220px;left:103px;color:var(--accent)}

/* add event */
.form{position:absolute;top:36px;left:8px;right:8px}
.field{height:19px;border-bottom:.6px solid var(--hairline);display:flex;align-items:center;padding:0 6px;font-size:5.4px;color:var(--muted);background:linear-gradient(#FCFCFD,#FCFCFD)}
.field svg{margin-left:auto;color:var(--accent);width:8px;height:8px}
.image-drop{margin:9px 6px 0;height:38px;border:.8px dashed var(--accent);border-radius:3px;display:flex;align-items:center;justify-content:center;gap:3px;color:var(--accent);font-size:5.4px}
</style>
</head>
<body>

<svg width="0" height="0" style="position:absolute">
  <defs>
    <symbol id="i-pin" viewBox="0 0 12 12"><path d="M6 11s4-3.8 4-6.3A4 4 0 0 0 2 4.7C2 7.2 6 11 6 11z"/><circle cx="6" cy="4.8" r="1.4"/></symbol>
    <symbol id="i-cal" viewBox="0 0 12 12"><rect x="1.5" y="2.5" width="9" height="8" rx="1"/><path d="M1.5 5h9M4 1.2v2.3M8 1.2v2.3"/></symbol>
    <symbol id="i-home" viewBox="0 0 12 12"><path d="M1.5 5.5 6 1.8l4.5 3.7V10.5h-9z"/></symbol>
    <symbol id="i-search" viewBox="0 0 12 12"><circle cx="5.3" cy="5.3" r="3.8"/><path d="m8.2 8.2 2.5 2.5"/></symbol>
    <symbol id="i-plus-circle" viewBox="0 0 12 12"><circle cx="6" cy="6" r="4.7"/><path d="M6 3.6v4.8M3.6 6h4.8"/></symbol>
    <symbol id="i-chat" viewBox="0 0 12 12"><rect x="1.3" y="2" width="9.4" height="7.5" rx="2"/><path d="M4.3 5.8h.1M7.7 5.8h.1"/></symbol>
    <symbol id="i-clock" viewBox="0 0 12 12"><circle cx="6" cy="6" r="4.7"/><path d="M6 3.5V6l1.8 1.2"/></symbol>
    <symbol id="i-add-user" viewBox="0 0 12 12"><circle cx="5" cy="4" r="2.3"/><path d="M1.5 10.5a3.5 3.5 0 0 1 6 -2.3M9.5 7.5v3M8 9h3"/></symbol>
    <symbol id="i-send" viewBox="0 0 12 12"><path d="M2.5 2 10 6l-7.5 4z"/></symbol>
    <symbol id="i-back" viewBox="0 0 12 12"><path d="M7.5 2 3.5 6l4 4"/></symbol>
    <symbol id="i-plus" viewBox="0 0 12 12"><path d="M6 2v8M2 6h8"/></symbol>
    <symbol id="i-filter" viewBox="0 0 12 12"><path d="M2 3.5h8M3.5 6h5M5 8.5h2"/></symbol>
    <symbol id="i-tag" viewBox="0 0 12 12"><path d="M6.5 1.5h4v4l-5 5-4-4z"/><circle cx="8.5" cy="3.5" r=".6"/></symbol>
    <symbol id="i-map" viewBox="0 0 12 12"><path d="M1.5 3 4.5 2 7.5 3.3 10.5 2v7L7.5 10.3 4.5 9 1.5 10z"/></symbol>
  </defs>
</svg>

<!-- Home -->
<section class="screen" style="left:65px;top:50px">
  <div class="status"><span>9:41</span><span class="signal"><i></i><i></i></span></div>
  <h1 class="screen-title">Home</h1>
  <nav class="home-tabs"><span>Popular</span><span>Featured</span><span>Upcoming</span><span>Trending</span></nav>

  <article class="event-card" style="top:74px">
    <div class="event-photo" role="img" aria-label="Conference hall with projector screens"><span class="badge">Popular</span><span class="countdown">5hrs 30mins</span></div>
    <div class="event-info">
      <h3>Pomel's Meetup</h3>
      <div class="meta-row"><i class="avatar"></i>Mike Hart<em>Organizer</em></div>
      <div class="meta-row place"><svg class="icon"><use href="#i-pin"/></svg>Pomel's Headquarters, NYC</div>
      <div class="meta-row date"><svg class="icon"><use href="#i-cal"/></svg>13/02/2020<span class="attendees"><i></i><i></i><b>+9</b></span></div>
    </div>
  </article>

  <article class="event-card" style="top:175px">
    <div class="event-photo concert" role="img" aria-label="Concert crowd under stage lights"><span class="badge">Popular</span><span class="countdown">3 Days</span></div>
    <div class="event-info">
      <h3>Musical Night</h3>
      <div class="meta-row"><i class="avatar"></i>Justin Richards<em>Organizer</em></div>
      <div class="meta-row place"><svg class="icon"><use href="#i-pin"/></svg>Downtown, California</div>
      <div class="meta-row date"><svg class="icon"><use href="#i-cal"/></svg>17/02/2020<span class="attendees"><i></i><i></i><b>+9</b></span></div>
    </div>
  </article>

  <nav class="tab-bar"><svg class="icon active"><use href="#i-home"/></svg><svg class="icon"><use href="#i-search"/></svg><svg class="icon"><use href="#i-plus-circle"/></svg><svg class="icon"><use href="#i-chat"/></svg><span class="me" role="img" aria-label="Profile photo"></span></nav>
  <div class="home-indicator"></div>
</section>

<!-- Event Overview -->
<section class="screen" style="left:295px;top:50px">
  <div class="status" style="color:var(--white)"><span></span><span class="signal"><i></i><i></i></span></div>
  <div class="hero" role="img" aria-label="Conference hall with projector screens">
    <span class="hero-back"><svg class="icon"><use href="#i-back"/></svg></span>
    <div class="hero-title">Event Overview</div>
    <span class="countdown">5hrs 30mins</span>
    <div class="dots"><i></i><i></i><i></i><i></i></div>
  </div>
  <div class="organizer-band"><span class="avatar" role="img" aria-label="Organizer portrait"></span><strong>Mike Hart</strong><svg class="icon"><use href="#i-add-user"/></svg></div>
  <div class="overview-body">
    <div class="overview-head"><h2>Pomel's Meetup</h2><span class="badge">Popular</span></div>
    <p>Pellentesque habitant morbi tristique senectus et netus et malesuada fames ac turpis egestas. Ut arcu libero, pulvinar non</p>
    <div class="meta-row place"><svg class="icon"><use href="#i-pin"/></svg>&nbsp;Pomel's Headquarters, NYC<span class="view-map">View Map</span><svg class="icon"><use href="#i-map"/></svg></div>
    <div class="meta-row date"><svg class="icon"><use href="#i-cal"/></svg>&nbsp;13/02/2020<span class="attendees"><i></i><i></i><i></i><b>+9</b></span></div>
    <div class="meta-row place" style="gap:3px"><svg class="icon"><use href="#i-tag"/></svg>&nbsp;<span class="tag">Event</span><span class="tag">Pomel</span><span class="tag">Meetup</span></div>
  </div>
  <div class="btn-primary" style="top:270px">Chat Now</div>
  <div class="home-indicator"></div>
</section>

<!-- Inbox -->
<section class="screen" style="left:525px;top:50px">
  <div class="status"><span>9:41</span><span class="signal"><i></i><i></i></span></div>
  <h1 class="screen-title">Inbox</h1>
  <div class="thread" style="top:44px"><span class="avatar" style="background:#3A3330" role="img" aria-label="Portrait"></span><div class="thread-body"><div class="thread-top">Mike Hart<em>(Pomel's Meetup)</em><time>Today</time></div><div class="thread-msg unread">Duis rhoncus dui venenatis<span class="unread-count">3</span></div></div></div>
  <div class="thread" style="top:75px"><span class="avatar" style="background:#A8423E" role="img" aria-label="Portrait"></span><div class="thread-body"><div class="thread-top">Sandra Patel<em>(Musical)</em><time>Yesterday</time></div><div class="thread-msg">Phasellus finibus enim nulla,</div></div></div>
  <div class="thread" style="top:106px"><span class="avatar" style="background:#6B3A4A" role="img" aria-label="Portrait"></span><div class="thread-body"><div class="thread-top">Kelly Holland<em>(Birthday)</em><time>18/02/2020</time></div><div class="thread-msg">Proin ac quam et lectus</div></div></div>
  <div class="thread" style="top:137px"><span class="avatar" style="background:#6F8294" role="img" aria-label="Portrait"></span><div class="thread-body"><div class="thread-top">Bruce Alvarado<em>(Bonfire)</em><time>18/02/2020</time></div><div class="thread-msg">You: Aliquam faucibus, odio</div></div></div>
  <div class="thread" style="top:168px;border:0"><span class="avatar" style="background:#4E5560" role="img" aria-label="Portrait"></span><div class="thread-body"><div class="thread-top">Rose Fox<em>(Skateboard)</em><time>18/02/2020</time></div><div class="thread-msg">Phasellus finibus enim nulla,</div></div></div>
  <nav class="tab-bar"><svg class="icon"><use href="#i-home"/></svg><svg class="icon"><use href="#i-search"/></svg><svg class="icon"><use href="#i-plus-circle"/></svg><svg class="icon active"><use href="#i-chat"/></svg><span class="me" role="img" aria-label="Profile photo"></span></nav>
  <div class="home-indicator"></div>
</section>

<!-- Chat -->
<section class="screen" style="left:65px;top:445px">
  <div class="status"><span>9:41</span><span class="signal"><i></i><i></i></span></div>
  <span class="chat-back"><svg class="icon"><use href="#i-back"/></svg></span>
  <div class="chat-head"><strong>Mike Hart</strong><em>(Pomel's Meetup)</em></div>
  <span class="chat-more">···</span>
  <span class="chat-avatar" role="img" aria-label="Organizer portrait"></span>
  <span class="chat-face" style="top:73px;left:7px" role="img" aria-label="Sender portrait"></span>
  <div class="bubble mine" style="top:73px">Hey Samantha, how are you?<time>2:03 PM</time></div>
  <span class="chat-face" style="top:104px;left:129px" role="img" aria-label="Sender portrait"></span>
  <div class="bubble theirs" style="top:104px">Hey George, I'm good.<br>How are you? Are you planning for a event.<time style="margin-top:9px">4:03 PM</time></div>
  <span class="chat-face" style="top:156px;left:7px" role="img" aria-label="Sender portrait"></span>
  <div class="bubble mine" style="top:156px">Yeah sure I'll let you know.<time>4:15 PM</time></div>
  <div class="composer"><svg class="icon"><use href="#i-plus"/></svg>Type something...</div>
  <div class="send-btn"><svg class="icon"><use href="#i-send"/></svg></div>
  <div class="home-indicator"></div>
</section>

<!-- Search list -->
<section class="screen" style="left:295px;top:445px">
  <div class="status"><span>9:41</span><span class="signal"><i></i><i></i></span></div>
  <h1 class="screen-title">Search</h1>
  <div class="segmented"><span class="on">List</span><span>Map</span></div>
  <div class="search-field"><svg class="icon"><use href="#i-search"/></svg>Search<svg class="icon"><use href="#i-filter"/></svg></div>
  <div class="results">
    <article class="event-card" style="top:2px">
      <div class="event-photo" role="img" aria-label="Conference hall with projector screens"><span class="badge">Popular</span><span class="countdown">5hrs 30mins</span></div>
      <div class="event-info">
        <h3>Pomel's Meetup</h3>
        <div class="meta-row"><i class="avatar"></i>Mike Hart<em>Organizer</em></div>
        <div class="meta-row place"><svg class="icon"><use href="#i-pin"/></svg>Pomel's Headquarters, NYC</div>
        <div class="meta-row date"><svg class="icon"><use href="#i-cal"/></svg>13/02/2020<span class="attendees"><i></i><i></i><b>+9</b></span></div>
      </div>
    </article>
    <article class="event-card" style="top:105px">
      <div class="event-photo concert" role="img" aria-label="Concert crowd under stage lights"><span class="badge">Popular</span><span class="countdown">3 Days</span></div>
      <div class="event-info">
        <h3>Musical Night</h3>
        <div class="meta-row"><i class="avatar"></i>Justin Richards<em>Organizer</em></div>
      </div>
    </article>
  </div>
  <nav class="tab-bar"><svg class="icon"><use href="#i-home"/></svg><svg class="icon active"><use href="#i-search"/></svg><svg class="icon"><use href="#i-plus-circle"/></svg><svg class="icon"><use href="#i-chat"/></svg><span class="me" role="img" aria-label="Profile photo"></span></nav>
  <div class="home-indicator"></div>
</section>

<!-- Search map -->
<section class="screen" style="left:525px;top:445px">
  <div class="status"><span>9:41</span><span class="signal"><i></i><i></i></span></div>
  <h1 class="screen-title">Search</h1>
  <div class="segmented"><span>List</span><span class="on">Map</span></div>
  <div class="search-field"><svg class="icon"><use href="#i-search"/></svg>Search<svg class="icon"><use href="#i-filter"/></svg></div>
  <div class="map-area" role="img" aria-label="Street map of the neighbourhood"></div>
  <article class="event-card map-card">
    <div class="event-photo" role="img" aria-label="Conference hall with projector screens"><span class="badge">Popular</span><span class="countdown">5hrs 30mins</span></div>
    <div class="event-info">
      <h3>Pomel's Meetup</h3>
      <div class="meta-row"><i class="avatar"></i>Mike Hart<em>Organizer</em></div>
      <div class="meta-row place"><svg class="icon"><use href="#i-pin"/></svg>Pomel's Headquarters, NYC</div>
      <div class="meta-row date"><svg class="icon"><use href="#i-cal"/></svg>13/02/2020<span class="attendees"><i></i><i></i><b>+9</b></span></div>
    </div>
  </article>
  <span class="you-pin"><svg class="icon"><use href="#i-pin"/></svg></span>
  <span class="map-pin"><svg class="icon"><use href="#i-pin"/></svg></span>
  <nav class="tab-bar"><svg class="icon"><use href="#i-home"/></svg><svg class="icon active"><use href="#i-search"/></svg><svg class="icon"><use href="#i-plus-circle"/></svg><svg class="icon"><use href="#i-chat"/></svg><span class="me" role="img" aria-label="Profile photo"></span></nav>
  <div class="home-indicator"></div>
</section>

<!-- Add Event -->
<section class="screen" style="left:295px;top:840px">
  <div class="status"><span>9:41</span><span class="signal"><i></i><i></i></span></div>
  <h1 class="screen-title">Add Event</h1>
  <form class="form">
    <div class="field">Event Name</div>
    <div class="field">Event Description</div>
    <div class="field">Starts In<svg class="icon"><use href="#i-clock"/></svg></div>
    <div class="field">Date<svg class="icon"><use href="#i-cal"/></svg></div>
    <div class="field">Location<svg class="icon"><use href="#i-pin"/></svg></div>
    <div class="field">Tags</div>
    <div class="field">Event Type</div>
    <div class="image-drop"><svg class="icon"><use href="#i-plus"/></svg>Add Images</div>
  </form>
  <div class="btn-primary" style="top:249px">Add Event</div>
  <nav class="tab-bar"><svg class="icon"><use href="#i-home"/></svg><svg class="icon"><use href="#i-search"/></svg><svg class="icon active"><use href="#i-plus-circle"/></svg><svg class="icon"><use href="#i-chat"/></svg><span class="me" role="img" aria-label="Profile photo"></span></nav>
  <div class="home-indicator"></div>
</section>

</body>
</html>
```